Slide Master for Harrowfield Engines - A Systematic Hedge Fund

We are looking for someone to produce a theme and slide master for us for our investor presentations. I have uploaded a few examples of templates that we would like to have included:
Main Title
Section Title
Slides with just bullet points
Different image/table configurations with bullet points and foot notes
Biographies of different lengths
A disclaimer (no one will read this but it should still look nice and needs to be in the presentations)
I have also uploaded the company logo, business card and colour definitions. Currently we have a blue colour scheme defined, but it would be nice to get a complementary set of colours so that when we have charts with more elements we can just draw from those.
The most important thing is that the slide master must be of general use to us. We arn't looking to have a specific presentation designed for us, but a theme/style that we can apply ourselves to any presentation we need to give in the future. It should have clearly defined guidelines for where content should go (and if this is different with and without footnotes for example). We would also like it to have a similar feel to the logo/business cards, so matt colours, high contrast, but not busy.
I'm excited to see the results!

```html
<!DOCTYPE html>
<html lang="en">
<head>
<meta charset="utf-8">
<title>Harrowfield Engines — Slide Master</title>
<link rel="stylesheet" href="https://fonts.googleapis.com/css2?family=Montserrat:wght@700;800&family=Roboto:wght@400&display=swap">
<style>
  :root {
    --canvas: #c8c8ca;
    --slide: #ffffff;
    --navy: #0c2d58;
    --accent: #4a86d4;
    --chart-bg: #b4cfee;
    --bar: #062f5f;
    --text: #3a3a3a;
    --muted: #222222;
  }
  * { box-sizing: border-box; margin: 0; padding: 0; }
  html, body { width: 1200px; height: 4032px; overflow: hidden; }
  body { background: var(--canvas); font-family: "Roboto", Arial, sans-serif; color: var(--text); position: relative; }

  .slide { position: absolute; left: 84px; width: 1047px; height: 588px; background: var(--slide); overflow: hidden; }
  .slide--about-section { top: 84px; }
  .slide--about { top: 718px; }
  .slide--chart-section { top: 1355px; }
  .slide--chart { top: 1996px; }
  .slide--bio-section { top: 2647px; }
  .slide--bio { top: 3301px; }

  .section-title { position: absolute; left: 0; right: 0; top: 250px; text-align: center; }
  .section-title h1 {
    display: inline-block; font-family: "Montserrat", Arial, sans-serif; font-weight: 800;
    font-size: 56px; line-height: 1; color: var(--navy); letter-spacing: 0.5px;
    padding: 0 4px 22px; border-bottom: 3px solid var(--accent);
  }

  .disclaimer { position: absolute; left: 11px; bottom: 14px; width: 780px; font-size: 8.3px; line-height: 11.5px; color: var(--muted); }

  .slide-header { position: absolute; left: 0; right: 0; top: 0; height: 89px; border-bottom: 2px solid var(--accent); }
  .slide-header h2 { position: absolute; top: 20px; font-family: "Montserrat", Arial, sans-serif; font-weight: 800; font-size: 22px; color: var(--navy); }
  .slide-header p { position: absolute; top: 50px; font-size: 14.5px; color: var(--text); }
  .brand-name { position: absolute; right: 22px; top: 34px; font-family: "Montserrat", Arial, sans-serif; font-weight: 800; font-size: 15px; letter-spacing: 0.6px; color: var(--navy); text-transform: uppercase; }

  .heading { font-family: "Montserrat", Arial, sans-serif; font-weight: 800; font-size: 18px; line-height: 27px; color: var(--navy); }
  .body-copy { font-size: 13.5px; line-height: 19.7px; color: var(--text); }

  .photo { position: absolute; left: 30px; top: 130px; width: 496px; height: 410px; background: linear-gradient(135deg, #2c3440 0%, #4a4f57 45%, #8a7a6c 75%, #c9b8a2 100%); }
  .about-text { position: absolute; left: 566px; top: 130px; width: 440px; }
  .about-text .body-copy { margin-top: 12px; }
  .tick-list { list-style: none; margin-top: 16px; }
  .tick-list li { position: relative; padding-left: 26px; font-size: 14px; line-height: 30.5px; color: var(--text); }
  .tick-list svg { position: absolute; left: 2px; top: 10px; }

  .chart-text { position: absolute; left: 38px; top: 131px; width: 420px; }
  .chart-text .heading + .body-copy { margin-top: 6px; }
  .chart-text .body-copy + .heading { margin-top: 38px; }
  .bar-chart { position: absolute; left: 480px; top: 155px; }

  .bio-col { position: absolute; width: 440px; }
  .bio-col .body-copy { margin-top: 10px; }
  .bio-col--l1 { left: 34px; top: 134px; }
  .bio-col--r1 { left: 535px; top: 134px; }
  .bio-col--l2 { left: 34px; top: 353px; }
  .bio-col--r2 { left: 535px; top: 353px; }
</style>
</head>
<body>

<section class="slide slide--about-section">
  <div class="section-title"><h1>ABOUT US</h1></div>
  <p class="disclaimer">Disclaimer : "Lorem Ipsum is simply dummy text of the printing and typesetting industry. Lorem Ipsum has been the industry's standard dummy text ever since the 1500s, when an unknown printer took a galley of type and scrambled it to make a type specimen book. It has survived not only five centuries,</p>
</section>

<section class="slide slide--about">
  <header class="slide-header">
    <h2 style="left:25px">ABOUT US</h2>
    <p style="left:23px">Lorem Ipsum is simply dummy text of the printing</p>
    <span class="brand-name">Harrowfield Engines</span>
  </header>
  <div class="photo" role="img" aria-label="Photo of hands typing on a laptop showing a trading chart"></div>
  <div class="about-text">
    <h3 class="heading">Lorem Ipsum is simply dummy text of the printing</h3>
    <p class="body-copy">But I must explain to you how all this mistaken idea of denouncing pleasure and praising pain was born and I will give you a complete account of the system, and expound the actual teachings of the great explorer of the truth, the master-builder of human happiness. No one rejects, dislikes, or avoids pleasure itself, because it is pleasure, but because those who do not know how to pursue pleasure rationally encounter consequences that are extremely</p>
    <ul class="tick-list">
      <li><svg width="11" height="9" viewBox="0 0 11 9"><path d="M1 4.5l3 3L10 1" fill="none" stroke="#0c2d58" stroke-width="2"/></svg>Lorem ipsum dolor sit amet</li>
      <li><svg width="11" height="9" viewBox="0 0 11 9"><path d="M1 4.5l3 3L10 1" fill="none" stroke="#0c2d58" stroke-width="2"/></svg>On the other hand, we denounce</li>
      <li><svg width="11" height="9" viewBox="0 0 11 9"><path d="M1 4.5l3 3L10 1" fill="none" stroke="#0c2d58" stroke-width="2"/></svg>But in certain circumstances and owing</li>
      <li><svg width="11" height="9" viewBox="0 0 11 9"><path d="M1 4.5l3 3L10 1" fill="none" stroke="#0c2d58" stroke-width="2"/></svg>Nam libero tempore, cum soluta nobis</li>
      <li><svg width="11" height="9" viewBox="0 0 11 9"><path d="M1 4.5l3 3L10 1" fill="none" stroke="#0c2d58" stroke-width="2"/></svg>But who has any right to find fault</li>
      <li><svg width="11" height="9" viewBox="0 0 11 9"><path d="M1 4.5l3 3L10 1" fill="none" stroke="#0c2d58" stroke-width="2"/></svg>Neque porro quisquam est,</li>
    </ul>
  </div>
  <p class="disclaimer">Disclaimer : "Lorem Ipsum is simply dummy text of the printing and typesetting industry. Lorem Ipsum has been the industry's standard dummy text ever since the 1500s, when an unknown printer took a galley of type and scrambled it to make a type specimen book. It has survived not only five centuries,</p>
</section>

<section class="slide slide--chart-section">
  <div class="section-title"><h1>CHART</h1></div>
  <p class="disclaimer">Disclaimer : "Lorem Ipsum is simply dummy text of the printing and typesetting industry. Lorem Ipsum has been the industry's standard dummy text ever since the 1500s, when an unknown printer took a galley of type and scrambled it to make a type specimen book. It has survived not only five centuries,</p>
</section>

<section class="slide slide--chart">
  <header class="slide-header">
    <h2 style="left:41px">CHART</h2>
    <p style="left:41px">Lorem Ipsum is simply dummy text of the printing</p>
    <span class="brand-name">Harrowfield Engines</span>
  </header>
  <div class="chart-text">
    <h3 class="heading">Lorem Ipsum is simply dummy</h3>
    <p class="body-copy">But I must explain to you how all this mistaken idea of denouncing pleasure and praising pain was born and I will give you a complete account of the system, and expound the actual teachings of the great explorer of the truth, the master-builder of human happiness. No one rejects, dislikes, or avoids pleasure itself, because it is pleasure, but because those who do not know how to pursue pleasure rationally encounter consequences that are extremely</p>
    <h3 class="heading">On the other hand, we denounce with</h3>
    <p class="body-copy">These cases are perfectly simple and easy to distinguish. In a free hour, when our power of choice is untrammelled and when nothing prevents our being able to do what we like best, every pleasure is to be welcomed and every pain avoided. But in certain circumstances and owing to the claims of duty or the obligations of business it will frequently occur that pleasures have to be repudiated and annoyances accepted.</p>
  </div>
  <svg class="bar-chart" width="560" height="340" viewBox="0 0 560 340" font-family="Roboto, Arial, sans-serif">
    <rect x="49" y="12" width="499" height="299" fill="#b4cfee"/>
    <g font-size="8.5" fill="#222" text-anchor="end">
      <text x="30" y="22">800</text><text x="30" y="57.5">700</text><text x="30" y="93">600</text>
      <text x="30" y="128.5">500</text><text x="30" y="164">400</text><text x="30" y="199.5">300</text>
      <text x="30" y="235">200</text><text x="30" y="270.5">100</text><text x="30" y="306">0</text>
    </g>
    <g fill="#062f5f">
      <rect x="53" y="273" width="25" height="30"/>
      <rect x="88" y="257" width="25" height="46"/>
      <rect x="124" y="243" width="25" height="60"/>
      <rect x="159" y="230" width="25" height="73"/>
      <rect x="195" y="188" width="25" height="115"/>
      <rect x="230" y="152" width="25" height="151"/>
      <rect x="266" y="70" width="25" height="233"/>
      <rect x="301" y="152" width="25" height="151"/>
      <rect x="337" y="163" width="25" height="140"/>
      <rect x="372" y="180" width="25" height="123"/>
      <rect x="408" y="200" width="25" height="103"/>
      <rect x="443" y="170" width="25" height="133"/>
      <rect x="479" y="227" width="25" height="76"/>
      <rect x="514" y="250" width="25" height="53"/>
    </g>
    <g font-size="7" fill="#222" text-anchor="middle">
      <text x="65" y="324">151-161</text><text x="100" y="324">161-171</text><text x="136" y="324">171-181</text>
      <text x="171" y="324">181-191</text><text x="207" y="324">191-201</text><text x="242" y="324">201-211</text>
      <text x="278" y="324">211-221</text><text x="313" y="324">221-231</text><text x="349" y="324">231-241</text>
      <text x="384" y="324">241-251</text><text x="420" y="324">251-261</text><text x="455" y="324">261-271</text>
      <text x="491" y="324">271-281</text><text x="526" y="324">281-291</text>
    </g>
  </svg>
  <p class="disclaimer">Disclaimer : "Lorem Ipsum is simply dummy text of the printing and typesetting industry. Lorem Ipsum has been the industry's standard dummy text ever since the 1500s, when an unknown printer took a galley of type and scrambled it to make a type specimen book. It has survived not only five centuries,</p>
</section>

<section class="slide slide--bio-section">
  <div class="section-title"><h1>BIOGRAPHIES</h1></div>
  <p class="disclaimer">Disclaimer : "Lorem Ipsum is simply dummy text of the printing and typesetting industry. Lorem Ipsum has been the industry's standard dummy text ever since the 1500s, when an unknown printer took a galley of type and scrambled it to make a type specimen book. It has survived not only five centuries,</p>
</section>

<section class="slide slide--bio">
  <header class="slide-header">
    <h2 style="left:30px">BIOGRAPHIES</h2>
    <p style="left:30px">Lorem Ipsum is simply dummy text of the printing</p>
    <span class="brand-name">Harrowfield Engines</span>
  </header>
  <div class="bio-col bio-col--l1">
    <h3 class="heading">Lorem Ipsum is simply dummy text</h3>
    <p class="body-copy">But I must explain to you how all this mistaken idea of denouncing pleasure and praising pain was born and I will give you a complete account of the system, and expound the actual teachings of the great explorer of the truth, the master-builder of human happiness. No one rejects, dislikes, or avoids pleasure itself, because it is pleasure, but because those who do not know how to pursue pleasure rationally encounter consequences that are extremely</p>
  </div>
  <div class="bio-col bio-col--r1">
    <h3 class="heading">Sed ut perspiciatis unde omnis iste natus</h3>
    <p class="body-copy">But I must explain to you how all this mistaken idea of denouncing pleasure and praising pain was born and I will give you a complete account of the system, and expound the actual teachings of the great explorer of the truth, the master-builder of human happiness. No one rejects, dislikes, or avoids pleasure itself, because it is pleasure, but because those who do not know how to pursue pleasure rationally encounter consequences that are extremely</p>
  </div>
  <div class="bio-col bio-col--l2">
    <h3 class="heading">Lorem Ipsum is simply dummy text</h3>
    <p class="body-copy">But I must explain to you how all this mistaken idea of denouncing pleasure and praising pain was born and I will give you a complete account of the system, and expound the actual teachings of the great explorer of the truth, the master-builder of human happiness. No one rejects, dislikes, or avoids pleasure itself, because it is pleasure, but because those who do not know how to pursue pleasure rationally encounter consequences that are extremely</p>
  </div>
  <div class="bio-col bio-col--r2">
    <h3 class="heading">Lorem ipsum dolor sit amet consectetur</h3>
    <p class="body-copy">But I must explain to you how all this mistaken idea of denouncing pleasure and praising pain was born and I will give you a complete account of the system, and expound the actual teachings of the great explorer of the truth, the master-builder of human happiness. No one rejects, dislikes, or avoids pleasure itself, because it is pleasure, but because those who do not know how to pursue pleasure rationally encounter consequences that are extremely</p>
  </div>
  <p class="disclaimer">Disclaimer : "Lorem Ipsum is simply dummy text of the printing and typesetting industry. Lorem Ipsum has been the industry's standard dummy text ever since the 1500s, when an unknown printer took a galley of type and scrambled it to make a type specimen book. It has survived not only five centuries,</p>
</section>

</body>
</html>
```